I need a two page flyer (one page front and back) outlining our residential furniture rental options.

Title: Premium Residential Furniture Rentals

GOOD
Our Brimwell Orla Furniture Package is designed to offer a perfect balance of affordability and style, without compromising on quality. This package features a selection of functional and aesthetically pleasing furniture pieces, ideal for those looking to create a polished and professional space. With quick installation handled by our experienced in-house team, you can expect a smooth and hassle-free setup. This package ensures both convenience and value, providing a streamlined solution for your needs.
Living room, dining room and bedroom (additional bedrooms available)
- $710/month with a 3 month commitment
- $570/month with a 6 month commitment

BETTER
Our Premium Furniture Package takes comfort and style to the next level, offering an enhanced experience compared to our Orla option. Carefully selected with durability in mind, this package features high-quality, convenient furniture designed for both functionality and aesthetics. Perfect for those seeking a more refined look and superior comfort, it’s ideal for creating a sophisticated and inviting environment. With attention to detail in both design and craftsmanship, the premium package elevates any space, ensuring a higher standard of comfort and style that caters to both employees and clients.
- $1,150/month with a 3 month commitment
- $900/month with a 6 month commitment

BEST
Our Custom Furniture Package offers a tailored experience where you’ll work directly with our expert designer to create the ultimate luxurious and functional space. We include lounging, dining, sleeping and working from home, this package allows you to curate a space that perfectly fits your needs and style. With personalized attention to detail, we ensure every element is designed to provide the highest level of comfort, convenience, and elegance, transforming your space into a sophisticated sanctuary for relaxation and enjoyment.
Please inquire for pricing

www.quilbyhomeleasing.com

```html
<!DOCTYPE html>
<html lang="en">
<head>
<meta charset="utf-8">
<title>Quilby Home Leasing – Residential Furniture Rentals</title>
<link rel="stylesheet" href="https://fonts.googleapis.com/css2?family=Oswald:wght@500;600&family=Open+Sans:ital,wght@0,400;0,600;1,400&family=Montserrat:wght@400;500&display=swap">
<style>
:root{
  --stage:#ababab;
  --paper:#ffffff;
  --slate:#58595b;
  --gold:#9a8150;
  --ink:#2b2b2b;
  --muted:#6b6b6b;
  --photo-a:#d9d6d0;
  --photo-b:#8f8a82;
}
*{box-sizing:border-box;margin:0;padding:0}
html,body{width:1200px;height:2226px;overflow:hidden;background:var(--stage)}
.page{position:absolute;left:236px;width:729px;height:1030px;background:var(--paper);overflow:hidden}
.page-front{top:58px}
.page-back{top:1138px}
.abs{position:absolute}

/* brand */
.brand{position:absolute;left:0;width:100%;text-align:center;font-family:"Montserrat",sans-serif;color:var(--ink)}
.brand-mark{width:44px;height:44px;border:3px solid var(--ink);margin:0 auto 14px}
.brand-name{font-size:25px;font-weight:500;letter-spacing:1px}
.brand-sub{display:flex;align-items:center;justify-content:center;gap:14px;font-size:13px;letter-spacing:11px;margin-top:6px}
.brand-sub::before,.brand-sub::after{content:"";width:40px;height:1.5px;background:var(--ink)}
.brand-tag{font-size:10px;font-weight:500;letter-spacing:1px;margin-top:8px}

.photo{position:absolute;background:linear-gradient(135deg,var(--photo-a),var(--photo-b))}

.title{position:absolute;font-family:"Oswald",sans-serif;font-weight:600;color:#fff;font-size:50px;line-height:53px;text-transform:uppercase}

.tab{position:absolute;background:var(--gold);color:#fff;font-family:"Oswald",sans-serif;font-weight:600;display:flex;align-items:center;justify-content:center;border-radius:0 40px 0 40px;box-shadow:4px 4px 6px rgba(0,0,0,.25)}
.price{position:absolute;font-family:"Oswald",sans-serif;font-weight:500;font-size:34px;line-height:36px}
.price small{display:block;font-family:"Open Sans",sans-serif;font-weight:400;font-size:14px;line-height:18px;letter-spacing:.3px}
.price-light{color:#fff}
.price-light small{color:#e6e6e6}
.price-gold{color:var(--gold)}
.price-gold small{color:var(--muted)}

.copy{position:absolute;font-family:"Open Sans",sans-serif;font-size:12px;line-height:14.6px;text-align:justify;color:var(--ink)}
.copy em{font-style:italic}
.copy-light{color:#fff}

.url-bar{position:absolute;background:var(--slate);color:#fff;font-family:"Open Sans",sans-serif;font-weight:600;font-size:17px;letter-spacing:2.5px;display:flex;align-items:center;justify-content:center;border-radius:0 16px 0 16px;box-shadow:4px 4px 6px rgba(0,0,0,.25)}
</style>
</head>
<body>

<section class="page page-front">
  <header class="brand" style="top:36px">
    <div class="brand-mark"></div>
    <div class="brand-name">QUILBY HOME</div>
    <div class="brand-sub">LEASING</div>
    <div class="brand-tag">STAGING | RESIDENTIAL | CORPORATE | SALES</div>
  </header>

  <div class="abs" style="left:339px;top:264px;width:347px;height:292px;background:var(--slate);border-radius:0 0 70px 0"></div>
  <div class="photo" role="img" aria-label="Bright furnished living room with armchair, gold side table and balcony doors" style="left:41px;top:227px;width:323px;height:368px;border-radius:70px 0 70px 0"></div>
  <h1 class="title" style="left:408px;top:296px">Premium<br>Residential<br>Furniture<br>Rentals</h1>

  <div class="abs" style="left:41px;top:728px;width:299px;height:262px;background:var(--slate);border-radius:0 80px 0 70px"></div>
  <div class="tab" style="left:92px;top:633px;width:162px;height:110px;font-size:60px">GOOD</div>
  <div class="price price-light" style="left:92px;top:804px">$710/MONTH<small>with a 3 month commitment</small></div>
  <div class="price price-light" style="left:92px;top:888px">$570/MONTH<small>with a 6 month commitment</small></div>

  <p class="copy" style="left:365px;top:726px;width:323px"><em>Our Brimwell Orla Furniture Package is designed to offer a perfect balance of affordability and style, without compromising on quality.</em> This package features a selection of functional and aesthetically pleasing furniture pieces, ideal for those looking to create a polished and professional space. With quick installation handled by our experienced in-house team, you can expect a smooth and hassle-free setup. This package ensures both convenience and value, providing a streamlined solution for your needs.<br>Living room, dining room and bedroom (additional bedrooms available)</p>

  <div class="abs" style="left:497px;top:953px;width:232px;height:32px;background:var(--gold);border-radius:16px 0 0 0"></div>
</section>

<section class="page page-back">
  <div class="photo" role="img" aria-label="Open-plan apartment with kitchen, bedroom and console table with round mirror" style="left:36px;top:79px;width:658px;height:368px;border-radius:80px 0 0 0"></div>

  <div class="abs" style="left:215px;top:34px;width:189px;height:131px;background:var(--paper);border-radius:0 30px 0 30px;box-shadow:4px 4px 8px rgba(0,0,0,.25)"></div>
  <header class="brand" style="top:62px;left:215px;width:189px">
    <div class="brand-mark" style="width:26px;height:26px;border-width:2px;margin-bottom:8px"></div>
    <div class="brand-name" style="font-size:13px;letter-spacing:.5px">QUILBY HOME</div>
    <div class="brand-sub" style="font-size:7px;letter-spacing:6px;gap:8px;margin-top:3px">LEASING</div>
    <div class="brand-tag" style="font-size:5px;margin-top:4px">STAGING | RESIDENTIAL | CORPORATE | SALES</div>
  </header>

  <div class="abs" style="left:61px;top:350px;width:300px;height:312px;background:var(--slate);opacity:.96;border-radius:0 0 0 60px"></div>
  <p class="copy copy-light" style="left:80px;top:360px;width:257px"><em>Our Premium Furniture Package takes comfort and style to the next level, offering an enhanced experience compared to our Orla option.</em> Carefully selected with durability in mind, this package features high-quality, convenient furniture designed for both functionality and aesthetics. Perfect for those seeking a more refined look and superior comfort, it’s ideal for creating a sophisticated and inviting environment. With attention to detail in both design and craftsmanship, the premium package elevates any space, ensuring a higher standard of comfort and style that caters to both employees and clients.<br>Living room, dining room and bedroom (additional bedrooms available)</p>

  <div class="tab" style="left:426px;top:385px;width:246px;height:110px;font-size:62px;background:var(--paper);color:var(--slate);border-radius:40px 0 40px 0">BETTER</div>
  <div class="price price-gold" style="left:434px;top:523px">$1,150/MONTH<small>with a 3 month commitment</small></div>
  <div class="price price-gold" style="left:434px;top:606px">$900/MONTH<small>with a 6 month commitment</small></div>

  <div class="tab" style="left:85px;top:631px;width:161px;height:147px;font-size:60px;border-radius:40px 0 0 0">BEST</div>
  <p class="copy" style="left:274px;top:719px;width:420px"><em>Our Custom Furniture Package offers a tailored experience where you’ll work directly with our expert designer to create the ultimate luxurious and functional space.</em> We include lounging, dining, sleeping and working from home, this package allows you to curate a space that perfectly fits your needs and style. With personalized attention to detail, we ensure every element is designed to provide the highest level of comfort, convenience, and elegance, transforming your space into a sophisticated sanctuary for relaxation and enjoyment.</p>

  <div class="price price-gold" style="left:123px;top:866px">$1,150/MONTH<small style="font-size:12px">with a 3 month commitment</small></div>
  <div class="price price-gold" style="left:445px;top:866px">$900/MONTH<small style="font-size:12px">with a 6 month commitment</small></div>

  <div class="url-bar" style="left:123px;top:954px;width:485px;height:34px">www.quilbyhomeleasing.com</div>
</section>

</body>
</html>
```